Upbeat Accouting Package Flyer

I am looking for a 1 page (front, or front and back) flyer that will become our marketing for our accounting services. We are looking for something a little different and we are catering to the small retail shop owners. We have 3 accounting packages we would like to display and then some add-ons. I have included our logo that must be included in the design. I have uploaded the accounting package information as well.
Target Market(s)
Small Retail Shop Owners
Industry/Entity Type
Accounting
Colors
Designer to choose colors to be used in the design.
Requirements
Must have
- A casual feel. We are not your typical accountants who are very professional and "stuffy". I want it to feel like we are all family.
Nice to have
- I would like to incorporate some sort of retail theme.
- We have a couple of taglines we like to use and it would be great if they could be included. They are "We know you CAN do the accounting, but do you WANT to?" and "We allow you to get back to what's important."
Should not have
- Typical stock accounting photos of people shaking hands, large office buildings, etc.

```html
<!DOCTYPE html>
<html lang="en">
<head>
<meta charset="utf-8">
<title>Brightway Tax and Accounting – Packages Flyer</title>
<link rel="stylesheet" href="https://fonts.googleapis.com/css2?family=Open+Sans:wght@400;600;700&family=Poppins:wght@500&display=swap">
<style>
  :root{
    --brand-blue:#1aa9dc;
    --brand-blue-deep:#0f8fc2;
    --card-blue:#19ade0;
    --ink-dark:#353535;
    --white:#ffffff;
    --page:#f2f2f2;
    --hero-warm-1:#8a6b55;
    --hero-warm-2:#c9b8a6;
    --hero-cool:#6f8796;
  }
  *{box-sizing:border-box;margin:0;padding:0}
  html,body{width:996px;height:1200px;overflow:hidden;background:var(--page)}
  body{font-family:"Open Sans",Arial,sans-serif;color:var(--white)}
  .flyer{position:relative;width:996px;height:1200px;background:var(--white);overflow:hidden}

  /* Hero */
  .hero-photo{position:absolute;left:0;top:0;width:996px;height:520px;
    background:linear-gradient(100deg,var(--hero-warm-1) 0%,var(--hero-warm-2) 45%,var(--hero-cool) 75%,#4f6472 100%)}
  .hero-shade{position:absolute;left:0;top:0;width:600px;height:520px;
    background:linear-gradient(90deg,rgba(40,30,25,.55),rgba(40,30,25,0))}
  .hero-curve{position:absolute;left:0;top:440px;width:996px;height:120px}

  .brand{position:absolute;left:52px;top:52px}
  .brand-name{font-family:"Poppins",sans-serif;font-weight:500;font-size:96px;line-height:1;color:var(--white);letter-spacing:1px}
  .brand-sub{font-family:"Open Sans",sans-serif;font-size:19px;color:var(--brand-blue);letter-spacing:.5px;margin:4px 0 0 150px}

  .tagline{position:absolute;left:52px;top:208px;width:480px}
  .quote-mark{position:absolute;left:0;top:-22px;font-family:Georgia,serif;font-size:110px;font-weight:700;color:var(--brand-blue);line-height:1}
  .tagline-main{margin-left:72px;font-size:30px;font-weight:600;line-height:44px}
  .tagline-rule{margin:8px 0 0 72px;width:270px;height:2px;background:var(--brand-blue)}
  .tagline-sub{margin:10px 0 0 72px;font-size:21px;font-weight:600;line-height:30px;text-transform:uppercase}

  /* Packages */
  .packages{position:absolute;left:20px;top:560px;display:flex;gap:16px}
  .package{position:relative;width:308px;height:478px;background:var(--card-blue);border-radius:12px;
    border:2px solid #d6eef8;padding:76px 14px 0 16px;box-shadow:0 8px 14px rgba(0,0,0,.12)}
  .package-badge{position:absolute;left:50%;top:-60px;width:118px;height:118px;margin-left:-59px;border-radius:50%;
    background:var(--white);box-shadow:0 4px 8px rgba(0,0,0,.2);display:flex;align-items:center;justify-content:center}
  .package-badge svg{width:100px;height:100px}
  .package-title{text-align:center;font-size:25px;font-weight:700;letter-spacing:.5px;line-height:30px}
  .package-note{text-align:center;font-size:13px;font-weight:700;line-height:16px}
  .package-list{list-style:none;margin-top:16px;font-size:14.5px;line-height:19.5px}
  .package-list.spaced{margin-top:4px}
  .package-list li{padding-left:11px;text-indent:-11px}
  .package-list li::before{content:"• "}

  /* Footer */
  .footer-band{position:absolute;left:0;top:1100px;width:996px;height:100px;background:var(--brand-blue)}
  .footer-dark{position:absolute;left:0;top:1052px;width:460px;height:148px}
  .options{position:absolute;left:38px;top:1070px}
  .options-title{font-size:16px;font-weight:700;color:var(--brand-blue);letter-spacing:.3px}
  .options-list{list-style:none;margin-top:6px;font-size:13.5px;line-height:18px}
  .options-list li::before{content:"• "}
  .contact{position:absolute;right:20px;top:1112px;text-align:right;font-size:16px;line-height:26px;font-style:normal}
  .contact-row{display:flex;justify-content:flex-end;align-items:center;gap:8px}
  .contact-row svg{width:20px;height:20px}
</style>
</head>
<body>
<div class="flyer">

  <div class="hero-photo" role="img" aria-label="Photo of a smiling shop owner in an apron standing arms crossed in a bakery with pastry cases"></div>
  <div class="hero-shade"></div>
  <svg class="hero-curve" viewBox="0 0 996 120" preserveAspectRatio="none" aria-hidden="true">
    <path d="M0 34 Q498 100 996 20 L996 120 L0 120 Z" fill="var(--brand-blue)"/>
    <path d="M0 50 Q498 112 996 38 L996 120 L0 120 Z" fill="var(--white)"/>
  </svg>

  <div class="brand">
    <div class="brand-name">brightway</div>
    <div class="brand-sub">TAX AND ACCOUNTING INC.</div>
  </div>

  <div class="tagline">
    <div class="quote-mark">“</div>
    <p class="tagline-main">We know you CAN do the accounting, but do you WANT to?</p>
    <div class="tagline-rule"></div>
    <p class="tagline-sub">We allow you to get back to what's important.</p>
  </div>

  <section class="packages">
    <article class="package">
      <div class="package-badge">
        <svg viewBox="0 0 100 100" aria-hidden="true">
          <circle cx="50" cy="50" r="48" fill="var(--brand-blue)"/>
          <circle cx="50" cy="43" r="14" fill="none" stroke="#fff" stroke-width="4"/>
          <rect x="43" y="58" width="14" height="5" fill="#fff"/>
          <rect x="44" y="65" width="12" height="3" fill="#fff"/>
          <rect x="46" y="70" width="8" height="3" fill="#fff"/>
        </svg>
      </div>
      <h2 class="package-title">DEVELOP</h2>
      <ul class="package-list">
        <li>$300/mo when paid annually</li>
        <li>$325/mo billed monthly</li>
        <li>LedgerLite Online subscription</li>
        <li>Free accounting setup</li>
        <li>Weekly transaction processing</li>
        <li>Monthly account reconciliation (up to 2 accounts)</li>
        <li>Monthly financial statements by the 15th of the month</li>
      </ul>
    </article>

    <article class="package">
      <div class="package-badge">
        <svg viewBox="0 0 100 100" aria-hidden="true">
          <circle cx="50" cy="50" r="48" fill="var(--brand-blue)"/>
          <rect x="28" y="58" width="8" height="14" fill="#fff"/>
          <rect x="40" y="50" width="8" height="22" fill="#fff"/>
          <rect x="52" y="42" width="8" height="30" fill="#fff"/>
          <rect x="64" y="34" width="8" height="38" fill="#fff"/>
          <path d="M26 52 L44 38 L54 44 L70 28" fill="none" stroke="#fff" stroke-width="3"/>
          <path d="M64 27 L72 26 L71 34 Z" fill="#fff"/>
        </svg>
      </div>
      <h2 class="package-title">GROW</h2>
      <ul class="package-list">
        <li>$550/mo billed annually</li>
        <li>$575/mo billed monthly</li>
        <li>LedgerLite Online subscription</li>
        <li>Free accounting setup</li>
        <li>Weekly transaction processing</li>
        <li>Monthly account reconciliation (up to 4 accounts)</li>
        <li>Monthly financial statements by the 10th of the month</li>
        <li>Client portal access for document sharing</li>
        <li>1 Custom Report</li>
        <li>Accounts Payable</li>
        <li>Monthly Scorecard (customized metric tracking for your business)</li>
      </ul>
    </article>

    <article class="package">
      <div class="package-badge">
        <svg viewBox="0 0 100 100" aria-hidden="true">
          <circle cx="50" cy="50" r="48" fill="var(--brand-blue)"/>
          <path d="M24 48 L50 70 L78 36" fill="none" stroke="#fff" stroke-width="4" stroke-linejoin="round"/>
          <path d="M30 46 L48 60 L70 42" fill="none" stroke="#fff" stroke-width="4" stroke-linecap="round"/>
          <circle cx="68" cy="32" r="5" fill="#fff"/>
        </svg>
      </div>
      <h2 class="package-title">RELAX</h2>
      <p class="package-note">(We've Got This)</p>
      <ul class="package-list spaced">
        <li>$850/mo billed annually</li>
        <li>$875/mo billed monthly</li>
        <li>LedgerLite Online subscription</li>
        <li>Free accounting setup</li>
        <li>Weekly transaction processing</li>
        <li>Monthly account reconciliation (up to 5-10 accounts)</li>
        <li>Monthly financial statements by the 5th of the month</li>
        <li>Client portal access for document sharing</li>
        <li>2 Custom Reports</li>
        <li>Accounts Payable</li>
        <li>Invoicing and accounts receivable</li>
        <li>Weekly Scorecard (customized metric tracking for your business)</li>
      </ul>
    </article>
  </section>

  <div class="footer-band"></div>
  <svg class="footer-dark" viewBox="0 0 460 148" preserveAspectRatio="none" aria-hidden="true">
    <path d="M0 0 Q250 0 460 148 L0 148 Z" fill="var(--ink-dark)"/>
  </svg>

  <div class="options">
    <h3 class="options-title">ADDITIONAL OPTIONS</h3>
    <ul class="options-list">
      <li>Payroll – 1-10 employees $85/mo</li>
      <li>11-30 employees $175/mo</li>
      <li>Sales tax - $30/mo per state</li>
      <li>Corporate taxes $50/mo</li>
      <li>Owner taxes - $25/mo</li>
    </ul>
  </div>

  <address class="contact">
    <div class="contact-row">(555) 204-7731
      <svg viewBox="0 0 20 20" aria-hidden="true"><circle cx="10" cy="10" r="9" fill="none" stroke="#fff" stroke-width="1.6"/><path d="M7 5.5 L8.6 5.5 L9.3 8 L8.2 9 Q9 11 11 11.8 L12 10.7 L14.5 11.4 L14.5 13 Q10 14 6.5 9.5 Q5.8 7 7 5.5Z" fill="#fff"/></svg>
    </div>
    <div class="contact-row">www.brightwaytax.com | hello@brightwaytax.com
      <svg viewBox="0 0 20 20" aria-hidden="true"><circle cx="10" cy="10" r="9" fill="none" stroke="#fff" stroke-width="1.6"/><circle cx="10" cy="10" r="2.5" fill="none" stroke="#fff" stroke-width="1.5"/><path d="M12.5 8 L12.5 11 Q12.5 13 14.5 12 Q15 8 12 6 Q8 5 6 8 Q5 12 8 14 Q10 15 12 14" fill="none" stroke="#fff" stroke-width="1.3"/></svg>
    </div>
    <div class="contact-row">4410 Maple Grove Ave, Springfield, KS 66000
      <svg viewBox="0 0 20 20" aria-hidden="true"><circle cx="10" cy="10" r="9" fill="none" stroke="#fff" stroke-width="1.6"/><path d="M10 15.5 Q6 11 6 8.5 A4 4 0 0 1 14 8.5 Q14 11 10 15.5Z" fill="#fff"/><circle cx="10" cy="8.5" r="1.5" fill="var(--brand-blue)"/></svg>
    </div>
  </address>

</div>
</body>
</html>
```